Website Landing Page for Brightfall Systems

Create a custom designed website landing page for our business. Looking for a professional upscale design that incorporates our logo and logo colors into the theme. I want a standard fixed frame website, not a constant scrolling format that seems to be the trend. To start with I'm looking for more of the graphic design part, maybe a concept or theme, I don't expect to see a finished project. Not interested in generic templates or layouts.

The name of our company is Brightfall Systems and I've attached our logo below. I'd like to have the web page have the same look and feel of our logo, as well as the colors. Our company, Brightfall Systems does system design, installation, and programming, of residential and commercial Audio/Video and Automation systems. We do home theaters, lighting and building automation, video conferencing systems, security camera installations, conference rooms, projectors, distributed audio systems, and similar Technology projects. This will be a professional services/informational website. We will not sell products on this website. This website will be used to advertise our company and communicate our services to prospective customers. Having a well designed, professional and clean website is one way we want to distinguish our company from the competition.

Here are some examples of what I consider a professional well designed website
http://www.qorlamstudio.com/Work/

Last year we had our tradlo store designed (with PixelMarket) and I'm really happy with the way it turned out. You can see it at www.HolvenGearDepot.com I consider this to be a great design and looking for the same level of quality with this new website. However, do not copy or use any part of this design in this new project. This tradlo store is completely separate from our other company Brightfall Systems. I only mention this tradlo store an an example of good work.

Reason: Still going through designs.

Reason: Still working on project and have not had time to review all designs and request revisions.

Reason: Sill going through designs and requesting revisions

Reason: still going through all the submissions we received.

Target Market(s)

People interested in Audio/Video, home theaters, home automation. We do sales, system design, and programming. We typically work on larger projects with both residential and commercial customers.

Industry/Entity Type

Business

Number of Pages Required

1 page

Requirements
Must have
• Great design elements. Please use a white background. I think white goes well with our logo colors.

```html
<!DOCTYPE html>
<html lang="en">
<head>
<meta charset="utf-8">
<title>Brightfall Systems</title>
<link href="https://fonts.googleapis.com/css2?family=PT+Sans:ital,wght@0,400;0,700;1,400&display=swap" rel="stylesheet">
<style>
:root{
  --blue:#5a88bb;
  --blue-band:rgba(74,128,196,.82);
  --green:#4cb81c;
  --text:#3c3c3c;
  --muted:#666;
  --white:#fff;
  --navy:#173a5c;
}
*{box-sizing:border-box;margin:0;padding:0}
html,body{width:1200px;height:2922px;overflow:hidden;background:var(--white)}
body{position:relative;font-family:"PT Sans",sans-serif;color:var(--text)}
.abs{position:absolute}
.top-strip{left:0;top:0;width:1200px;height:23px;background:#b9c3d6}
.hero{left:0;top:0;width:1200px;height:803px;background:linear-gradient(180deg,#aebfd2 0%,#c8d3de 22%,#7a8a76 40%,#4f7a34 62%,#3f6b3a 78%,#3c6a62 100%)}
.nav{left:0;top:23px;width:1200px;height:102px;background:rgba(255,255,255,.9)}
.brand{left:24px;top:36px;display:flex;align-items:center;gap:14px}
.brand-mark{width:70px;height:70px;border-radius:50%;border:6px solid #2a9fd6}
.brand-name{font-size:26px;font-weight:700;color:#2a9fd6;width:140px;line-height:1.05}
.nav-links{top:66px;left:0;display:flex;font-size:20px;color:#333}
.nav-links span{position:absolute;white-space:nowrap}
.hero-title{left:0;top:452px;width:1200px;text-align:center;color:var(--white);font-size:33px;font-weight:700;line-height:40px}
.hero-sub{left:0;top:548px;width:1200px;text-align:center;color:var(--white);font-size:33px;font-style:italic}
.btn{background:var(--green);color:var(--white);font-weight:700;border-radius:6px;display:flex;align-items:center;justify-content:center}
.hero-btn{left:518px;top:606px;width:198px;height:62px;font-size:24px}
.products-title{left:0;top:880px;width:1200px;text-align:center;color:var(--blue);font-size:51px;font-weight:400;letter-spacing:1px}
.products-sub{left:0;top:940px;width:1200px;text-align:center;color:#777;font-size:31px;font-style:italic}
.products-copy{left:115px;top:988px;width:1010px;text-align:center;color:#666;font-size:27px;line-height:31px}
.grid{left:80px;top:1128px;width:1054px;height:440px;display:grid;grid-template-columns:352px 352px 350px;grid-template-rows:220px 220px}
.tile{position:relative}
.tile-label{position:absolute;left:0;bottom:0;width:100%;height:44px;background:var(--blue-band);color:var(--white);font-size:26px;font-weight:700;display:flex;align-items:center;justify-content:center;letter-spacing:1px}
.news-title{left:48px;top:1666px;color:var(--blue);font-size:35px;font-weight:700}
.news-item{left:44px;width:378px}
.news-date{font-size:18px;color:#222}
.news-text{font-size:18px;font-style:italic;line-height:21px;margin-top:6px;color:#333}
.read-more{font-size:15px;font-weight:700;color:var(--green);text-decoration:underline}
.divider{left:26px;width:380px;height:2px;background:#c9d3df}
.more{left:187px;top:2222px;font-size:15px;color:var(--blue);font-weight:700;display:flex;gap:6px;align-items:center}
.feature-photo{left:467px;top:1679px;width:733px;height:302px;background:linear-gradient(180deg,#8fa8c6 0%,#c4d1de 45%,#b9bfc0 70%,#5e7a38 100%)}
.feature-head{left:470px;top:1998px;font-size:21px;font-weight:700;color:#111}
.feature-quote{left:470px;top:2035px;width:660px;font-size:21px;line-height:25px;color:#444}
.feature-btn{left:469px;top:2131px;width:141px;height:47px;font-size:20px}
.footer{left:0;top:2318px;width:1200px;height:382px;background:linear-gradient(160deg,#2d5a7c 0%,#1c4465 45%,#143656 100%)}
.on-dark{color:var(--white)}
.foot-name{left:18px;top:2380px;font-size:26px;font-weight:700}
.foot-line{left:24px;font-size:21px}
.foot-link{left:22px;top:2538px;font-size:18px;color:var(--green);text-decoration:underline}
.foot-btn{left:14px;top:2585px;width:140px;height:47px;font-size:20px}
.col-head{font-size:25px;font-weight:700;color:var(--green)}
.col-item{font-size:19px;color:var(--white)}
.legal{left:500px;top:2657px;font-size:14px;display:flex;gap:18px;color:var(--white)}
.legal u{text-decoration:underline}
.social{left:1032px;top:2625px;display:flex;gap:6px}
.social span{width:28px;height:28px;background:var(--green);border-radius:4px}
</style>
</head>
<body>
<div class="abs hero" role="img" aria-label="City skyline above a tree-lined canal"></div>
<div class="abs top-strip"></div>
<div class="abs nav"></div>
<div class="abs brand"><span class="brand-mark"></span><span class="brand-name">Brightfall Systems</span></div>
<nav class="abs nav-links">
  <span style="left:432px">Home</span>
  <span style="left:547px">Who we are</span>
  <span style="left:716px">Our Products</span>
  <span style="left:898px">Services</span>
  <span style="left:1044px">Contact</span>
</nav>
<h1 class="abs hero-title">Lorem ipsum dolor sit amet, consectetur adipiscing<br>elit. Vestibulum vel lacus id mauris suscipit</h1>
<p class="abs hero-sub">Brightfall Systems are for you</p>
<div class="abs btn hero-btn">learn more</div>

<h2 class="abs products-title">Experience our Products</h2>
<p class="abs products-sub">Brightfall Systems are for you</p>
<p class="abs products-copy">Lorem ipsum dolor sit amet, consectetur adipiscing elit. Ut viverra dolor pulvinar, semper justo at, euismod tortor. Morbi pretium convallis urna, eget tempus massa mattis sit amet. Suspendisse vel tellus tortor.</p>
<div class="abs grid">
  <div class="tile" role="img" aria-label="Conference room with long table and screen" style="background:linear-gradient(180deg,#e8e4e0,#8a6a5a 55%,#3a3a3a)"><div class="tile-label">Conferencing System</div></div>
  <div class="tile" role="img" aria-label="Living room home theater" style="background:linear-gradient(180deg,#f1e6c8,#c9b48a 55%,#6a5a44)"><div class="tile-label">Home Theater</div></div>
  <div class="tile" role="img" aria-label="Ornate hall with security coverage" style="background:linear-gradient(180deg,#d8c08a,#b08e54 55%,#7a6440)"><div class="tile-label">Secruity System</div></div>
  <div class="tile" role="img" aria-label="Lit bar interior" style="background:linear-gradient(180deg,#6a7a80,#2e3336 55%,#6a4030)"><div class="tile-label">Lighting Automation</div></div>
  <div class="tile" role="img" aria-label="Auditorium with projection screen" style="background:linear-gradient(180deg,#bfc3c6,#7a8088 55%,#3c4046)"><div class="tile-label">Projection</div></div>
  <div class="tile" role="img" aria-label="Glass office tower against blue sky" style="background:linear-gradient(160deg,#6f9fe0,#4a7cc8 50%,#2f5ea8)"><div class="tile-label">Buildings</div></div>
</div>

<h2 class="abs news-title">News and Information</h2>
<article class="abs news-item" style="top:1732px">
  <div class="news-date">June 12, 2017</div>
  <p class="news-text">Lorem ipsum dolor sit amet, consectetur adipiscing elit. Ut viverra dolor pulvinar, semper justo at, euismod tortor. Morbi pretium convallis urna, eget tempus massa mattis sit amet. Suspendisse vel tellus tortor.</p>
  <div class="read-more" style="margin-top:8px">Read More</div>
</article>
<div class="abs divider" style="top:1911px"></div>
<article class="abs news-item" style="top:1930px">
  <div class="news-date">June 17, 2017</div>
  <p class="news-text">Lorem ipsum dolor sit amet, consectetur adipiscing elit. Ut viverra dolor pulvinar, semper justo at, euismod tortor.</p>
  <div class="read-more" style="margin-top:16px">Read More</div>
</article>
<div class="abs divider" style="top:2077px"></div>
<article class="abs news-item" style="top:2085px">
  <div class="news-date">June 17, 2017</div>
  <p class="news-text">Lorem ipsum dolor sit amet, consectetur adipiscing elit. Ut viverra dolor pulvinar, semper justo at, euismod tortor.</p>
  <div class="read-more" style="margin-top:6px">Read More</div>
</article>
<div class="abs more"><svg width="22" height="12" viewBox="0 0 22 12"><path d="M0 0h22L11 12z" fill="#8fb0d8"/></svg>More</div>

<div class="abs feature-photo" role="img" aria-label="City skyline over treetops under a cloudy sky"></div>
<h3 class="abs feature-head">Lorem Ipsum</h3>
<p class="abs feature-quote">“Lorem ipsum dolor sit amet, consectetur adipiscing elit. Ut viverra dolor pulvinar, semper justo at, euismod tortor. Morbi pretium convallis urna, eget tempus massa mattis sit amet. “</p>
<div class="abs btn feature-btn">Learn More</div>

<footer class="abs footer" role="img" aria-label="Glass office building under a blue sky, darkened"></footer>
<div class="abs foot-name on-dark">Brightfall Systems</div>
<div class="abs foot-line on-dark" style="top:2420px">48 Larkmoor Ave.</div>
<div class="abs foot-line on-dark" style="top:2446px">Calverton, CA 90412</div>
<div class="abs foot-line on-dark" style="top:2480px;font-size:19px">(555) 014-2280</div>
<div class="abs foot-line on-dark" style="top:2505px;font-size:19px">(555) 014-2291</div>
<div class="abs foot-link">Get Directions</div>
<div class="abs btn foot-btn">Contact</div>

<div class="abs col-head" style="left:505px;top:2381px">About</div>
<div class="abs col-item" style="left:505px;top:2424px">History</div>
<div class="abs col-item" style="left:505px;top:2461px">The team</div>
<div class="abs col-item" style="left:505px;top:2498px">Careers</div>

<div class="abs col-head" style="left:686px;top:2381px">Services</div>
<div class="abs col-item" style="left:688px;top:2421px">Installations</div>
<div class="abs col-item" style="left:688px;top:2457px">Commercial</div>
<div class="abs col-item" style="left:692px;top:2493px">Residential</div>
<div class="abs col-item" style="left:690px;top:2528px">Project Management</div>

<div class="abs col-head" style="left:927px;top:2383px">Products</div>
<div class="abs col-item" style="left:929px;top:2426px">Projection</div>
<div class="abs col-item" style="left:929px;top:2463px">Home Theater</div>
<div class="abs col-item" style="left:929px;top:2500px">Buildings</div>
<div class="abs col-item" style="left:929px;top:2534px">Conferencing System</div>
<div class="abs col-item" style="left:929px;top:2569px">Security System</div>

<div class="abs legal"><span>All Rights Reserved</span><u>Privacy Policy</u><u>Terms of Use</u></div>
<div class="abs social" aria-label="Social links"><span></span><span></span><span></span><span></span></div>
</body>
</html>
```